plumweave business card

need to upgrade current business card for an online retailer of handmade arts and crafts, please visit plumweave.com.au

need to be artistic professional look

sample layout, contents, logo, are in the attached files

need for 4 people, details for other 2 people to be provided later

Industry/Entity Type

Business

```html
<!DOCTYPE html>
<html lang="en">
<head>
<meta charset="utf-8">
<title>PlumWeave Business Card</title>
<link rel="stylesheet" href="https://fonts.googleapis.com/css2?family=Source+Sans+3:wght@400;600;700&display=swap">
<style>
  :root {
    --bg: #ece9e4;
    --card-red: #d9402f;
    --card-white: #ffffff;
    --card-grey: #e4e4e4;
    --ink-dark: #2b2b2b;
    --ink-light: #ffffff;
    --shadow: rgba(0, 0, 0, 0.25);
  }
  * { box-sizing: border-box; margin: 0; padding: 0; }
  html, body {
    width: 1200px; height: 900px; overflow: hidden;
    background: var(--bg);
    font-family: "Source Sans 3", "Myriad Pro", Arial, sans-serif;
  }
  .canvas { position: relative; width: 1200px; height: 900px; }

  .card {
    position: absolute;
    width: 620px; height: 350px;
    border-radius: 3px;
    box-shadow: 0 8px 24px var(--shadow);
    overflow: hidden;
  }

  /* Front */
  .card-front { left: 70px; top: 80px; background: var(--card-red); }
  .front-header {
    position: absolute; left: 0; top: 0; width: 100%; height: 150px;
    background: linear-gradient(to bottom, var(--card-white) 0%, var(--card-white) 55%, var(--card-grey) 100%);
    text-align: center;
  }
  .brand-name {
    padding-top: 24px;
    font-weight: 700; font-size: 64px; line-height: 1;
    letter-spacing: -1px;
    color: var(--ink-dark);
  }
  .brand-tagline {
    margin-top: 8px;
    font-weight: 400; font-size: 24px; line-height: 1;
    color: var(--ink-dark);
  }
  .person {
    position: absolute; left: 60px; top: 195px; width: 250px;
    text-align: center; color: var(--ink-dark);
  }
  .person-name { font-weight: 600; font-size: 25px; line-height: 1.1; }
  .person-role { font-size: 17px; margin-top: 2px; }
  .contact {
    position: absolute; left: 390px; top: 162px;
    color: var(--ink-dark); font-size: 16px; line-height: 1.35;
  }

  /* Back */
  .card-back {
    left: 510px; top: 470px; background: var(--card-red);
    color: var(--ink-light);
  }
  .back-intro {
    position: absolute; top: 42px; left: 0; width: 100%;
    text-align: center; font-weight: 600; font-size: 17px;
  }
  .offer-list {
    position: absolute; top: 104px; left: 170px;
    list-style: none; font-size: 16px; line-height: 1.35;
  }
  .offer-list li:not(:first-child) { padding-left: 16px; }
  .back-mission {
    position: absolute; left: 40px; top: 262px; width: 460px;
    font-weight: 700; font-size: 19px; line-height: 1.3;
  }
</style>
</head>
<body>
<main class="canvas">
  <section class="card card-front">
    <header class="front-header">
      <div class="brand-name">PlumWeave</div>
      <div class="brand-tagline">handmade with heart</div>
    </header>
    <div class="person">
      <div class="person-name">Devan Rai</div>
      <div class="person-role">Director, PlumWeave Australia</div>
    </div>
    <div class="contact">
      <div>e devan@plumweave.com.au</div>
      <div>p +61 400 555 019</div>
    </div>
  </section>

  <section class="card card-back">
    <p class="back-intro">Visit us for exotic hand-made arts &amp; crafts around the globe</p>
    <ul class="offer-list">
      <li>Cashmere fashion items from Nepal</li>
      <li>-Thai Traditional Paintings</li>
      <li>-Nepali/Tibetan Thangkas</li>
      <li>-Lokta/Rice Paper Crafts</li>
      <li>-Allo/Cotton/Woolllen items</li>
    </ul>
    <p class="back-mission">We encourage eco-friendly, sustainable and traditional arts practice.</p>
  </section>
</main>
</body>
</html>
```